Marlow Crest Group (Real Estate and Investment)

A high end, clean design.
We are a real estate company with sales, asset management and investment divisions. We want to use a black and white scheme which is really high end feel. The back of the card can just be the logo (black background with the white writing) as we will probably emboss this when we print)

Target Market(s)

High level investors, high end houses for sale

Industry/Entity Type

Business

Contact Information for Business Card

Name, position, phone number and email address
Glen Varley, Managing Director, 0437259064 and glen@marlowcrest-example.com.au

Requirements
Must have
• Back of the card to be the black background with the white writing (as per the attached images). Would like the capacity to emboss the writing and logo

```html
<!DOCTYPE html>
<html lang="en">
<head>
<meta charset="UTF-8">
<title>Marlow Crest Group – Business Card</title>
<link rel="stylesheet" href="https://fonts.googleapis.com/css2?family=Arimo:wght@400;700&display=swap">
<style>
  :root {
    --backdrop: #d9d9d6;
    --card-white: #ffffff;
    --card-black: #231f20;
    --ink: #111111;
    --ink-soft: #222222;
    --paper-ink: #ffffff;
  }
  * { margin: 0; padding: 0; box-sizing: border-box; }
  html, body {
    width: 1200px;
    height: 1200px;
    overflow: hidden;
    background: var(--backdrop);
    font-family: "Arimo", Arial, sans-serif;
  }
  .sheet {
    width: 1200px;
    height: 1200px;
    display: flex;
    flex-direction: column;
    align-items: center;
    justify-content: center;
    gap: 60px;
  }
  .card {
    width: 820px;
    height: 500px;
    position: relative;
    box-shadow: 0 6px 18px rgba(0,0,0,0.18);
  }
  .card--front { background: var(--card-white); color: var(--ink); }
  .card--back { background: var(--card-black); color: var(--paper-ink); }

  .brand {
    position: absolute;
    display: flex;
    flex-direction: column;
    align-items: center;
    gap: 22px;
  }
  .brand__mark {
    width: 96px;
    height: 96px;
    border-radius: 50%;
    border: 2px solid currentColor;
  }
  .brand__name {
    font-size: 30px;
    font-weight: 400;
    letter-spacing: -0.5px;
    white-space: nowrap;
  }
  .card--front .brand { left: 56px; top: 150px; color: var(--ink-soft); }
  .card--back .brand { left: 50%; top: 50%; transform: translate(-50%, -50%); }

  .person {
    position: absolute;
    right: 56px;
    top: 168px;
    text-align: right;
  }
  .person__role { font-size: 17px; font-weight: 400; }
  .person__name {
    font-size: 40px;
    font-weight: 700;
    letter-spacing: -0.5px;
    line-height: 1.05;
    text-transform: uppercase;
  }

  .contact {
    position: absolute;
    right: 56px;
    bottom: 62px;
    list-style: none;
    display: flex;
    flex-direction: column;
    align-items: flex-end;
    gap: 12px;
    font-size: 17px;
  }
  .contact__item { display: flex; align-items: center; gap: 10px; }
  .contact__icon { width: 24px; height: 24px; display: block; }
</style>
</head>
<body>
<main class="sheet">
  <section class="card card--front" aria-label="Card front">
    <div class="brand">
      <span class="brand__mark" aria-hidden="true"></span>
      <span class="brand__name">MARLOW CREST GROUP</span>
    </div>
    <div class="person">
      <p class="person__role">Managing Director</p>
      <h1 class="person__name">Glen Varley</h1>
    </div>
    <ul class="contact">
      <li class="contact__item">
        <span>0437259064</span>
        <svg class="contact__icon" viewBox="0 0 24 24" aria-hidden="true">
          <circle cx="12" cy="12" r="12" fill="#333"/>
          <path d="M8.6 6.5c.4-.3 1-.2 1.2.3l1 2c.2.4.1.8-.2 1.1l-.8.7c.6 1.3 1.6 2.4 2.9 3l.7-.8c.3-.3.8-.4 1.1-.2l2 1c.5.2.6.8.3 1.2l-.9 1.2c-.4.5-1.1.7-1.7.5-3.4-1.1-6-3.7-7.1-7.1-.2-.6 0-1.3.5-1.7z" fill="#fff"/>
        </svg>
      </li>
      <li class="contact__item">
        <span>glen@marlowcrest-example.com.au</span>
        <svg class="contact__icon" viewBox="0 0 24 24" aria-hidden="true">
          <circle cx="12" cy="12" r="12" fill="#333"/>
          <rect x="6.5" y="8" width="11" height="8" rx="1" fill="#fff"/>
          <path d="M6.8 8.5l5.2 4 5.2-4" fill="none" stroke="#333" stroke-width="1.2"/>
        </svg>
      </li>
    </ul>
  </section>

  <section class="card card--back" aria-label="Card back">
    <div class="brand">
      <span class="brand__mark" aria-hidden="true"></span>
      <span class="brand__name">MARLOW CREST GROUP</span>
    </div>
  </section>
</main>
</body>
</html>
```